Talvin Foundation Letterhead

We are a newly established non profit registered in Maryland but operates in Africa, south of the sahara. We offer scholarships to deserving young adults from high school through college. Our color theme for our existing logo is purple, we want a design that is stylish, spellbinding yet a letterhead that projects seriousness. More information on www.thetalvinfoundation.org

Target Market(s)

High school and college students in sub saharan African as well as our donors in the US

Industry/Entity Type

Non Profit

Font styles to use
Script

Requirements
Must have
• Logo at the top and if possible watermark the logo in the middle of the letterhead, contact address,
Should not have
• NA

```html
<!DOCTYPE html>
<html lang="en">
<head>
<meta charset="utf-8">
<title>Talvin Foundation Letterhead</title>
<link rel="stylesheet" href="https://fonts.googleapis.com/css2?family=Cinzel:wght@400&family=Roboto:wght@400&display=swap">
<style>
  :root {
    --backdrop: #ececec;
    --paper: #ffffff;
    --purple: #6a3d9a;
    --purple-deep: #3f1460;
    --purple-light: #5c2d8c;
    --watermark: #f1eef5;
    --ink-grey: #8a8a8a;
  }
  html, body {
    margin: 0;
    width: 1200px;
    height: 898px;
    overflow: hidden;
    background: var(--backdrop);
  }
  .letterhead {
    position: absolute;
    left: 296px;
    top: 19px;
    width: 608px;
    height: 860px;
    background: var(--paper);
    box-shadow: 0 6px 24px rgba(0,0,0,0.12);
    overflow: hidden;
  }
  .brand {
    position: absolute;
    left: 62px;
    top: 118px;
    display: flex;
    align-items: center;
    gap: 10px;
  }
  .brand-dot {
    width: 14px;
    height: 14px;
    border-radius: 50%;
    background: var(--purple);
  }
  .brand-name {
    font-family: "Cinzel", serif;
    font-weight: 400;
    font-size: 19px;
    color: var(--purple);
    letter-spacing: 0.5px;
  }
  .tagline {
    position: absolute;
    left: 86px;
    top: 148px;
    font-family: "Roboto", sans-serif;
    font-size: 6.5px;
    letter-spacing: 1.6px;
    text-transform: uppercase;
    color: var(--purple);
  }
  .contact {
    position: absolute;
    right: 52px;
    top: 112px;
    list-style: none;
    margin: 0;
    padding: 0;
    font-family: "Roboto", sans-serif;
    font-size: 10px;
    color: var(--ink-grey);
    letter-spacing: 0.6px;
  }
  .contact li {
    display: flex;
    align-items: center;
    gap: 8px;
    margin-bottom: 5px;
  }
  .contact svg { width: 9px; height: 9px; fill: var(--purple); }
  .watermark {
    position: absolute;
    left: 214px;
    top: 300px;
    width: 300px;
    height: 300px;
    border-radius: 50%;
    border: 6px solid var(--watermark);
    box-sizing: border-box;
  }
  .footer-band {
    position: absolute;
    left: 0;
    bottom: 0;
    width: 608px;
    height: 260px;
  }
  .address {
    position: absolute;
    left: 150px;
    top: 770px;
    font-family: "Cinzel", serif;
    font-size: 11px;
    letter-spacing: 1.6px;
    color: #ffffff;
    transform: rotate(-17deg);
    transform-origin: left center;
    white-space: nowrap;
  }
</style>
</head>
<body>
  <main class="letterhead">
    <header>
      <div class="brand">
        <span class="brand-dot"></span>
        <span class="brand-name">The Talvin Foundation Inc</span>
      </div>
      <div class="tagline">Giving every child a chance at an education</div>
      <ul class="contact">
        <li><svg viewBox="0 0 10 10"><path d="M2 0.5l2 2-1 1.2c.6 1.3 1.6 2.3 2.9 2.9L7 5.6l2 2-1.3 1.8C4.3 9 1 5.7.6 2.1z"/></svg>0207 815 3362</li>
        <li><svg viewBox="0 0 10 10"><path d="M0 1.5h10v7H0zM1 2.5v.3l4 2.6 4-2.6v-.3zM1 4v3.5h8V4L5 6.5z"/></svg>info@talvinfoundation.com</li>
        <li><svg viewBox="0 0 10 10"><circle cx="5" cy="5" r="4.5"/></svg>www.talvinfoundation.com</li>
      </ul>
    </header>

    <div class="watermark" aria-hidden="true"></div>

    <svg class="footer-band" viewBox="0 0 608 260" aria-hidden="true">
      <path d="M0 260 L0 250 C180 120 380 40 608 0 L608 260 Z" fill="var(--purple-light)"/>
      <path d="M0 260 L0 255 C190 140 390 70 608 36 L608 260 Z" fill="var(--purple-deep)"/>
    </svg>
    <div class="address">Meridian Park Complex, Halvera, Indonesia 15210</div>
  </main>
</body>
</html>
```